Bright Arrow Delivery Service Wordpress design

My client is a delivery service whose motto is "We go where the freight leads us." Their colors are red, white and blue. They use Voyalo vans and box vans - NO semi tractors. They like this Website design www.tovamu-sample.com, but I would like to see some designs that make them stand out. Attached is their new logo.

Target Market(s)

Businesses who use delivery services in town and anyone needing freight picked up or transported in the United States.

Industry/Entity Type

Delivery Service

Number of Pages Required

1 page

Font styles to use
Sans Serif

Colors
ec1f27
0455a3
ffffff

Requirements
Must have
• We need a Wordpress design with sliders that incorporates their new logo and the motto "WE GO WHERE THE FREIGHT LEADS US" Their corporate colors are red, white and blue. They only use voyalo vans and box vans.
Nice to have
• Please use your creativity to come up with a unique design for this delivery service.
Should not have
• NO SEMI TRACTOR TRAILERS

```html
<!DOCTYPE html>
<html lang="en">
<head>
<meta charset="utf-8">
<title>Bright Arrow Express Delivery</title>
<link rel="stylesheet" href="https://fonts.googleapis.com/css2?family=Michroma&family=Open+Sans:wdth,wght@75..100,400..800&display=swap">
<style>
:root{
  --red:#ec1f27;
  --blue:#0455a3;
  --navy:#2a3547;
  --ink:#222;
  --text:#333;
  --muted:#777;
  --grey-band:#e6e6e6;
  --footer:#333333;
  --footer-line:#4a4a4a;
  --white:#fff;
}
*{box-sizing:border-box;margin:0;padding:0}
html,body{width:739px;height:1200px;overflow:hidden;background:var(--white)}
body{position:relative;font-family:"Open Sans",sans-serif;color:var(--text)}
.abs{position:absolute}
.wide{font-family:"Michroma",sans-serif}

/* top bar */
.topbar{left:61px;top:0;width:617px;height:30px;background:var(--navy)}
.topbar ul{list-style:none;display:flex;height:30px;align-items:center;padding-left:16px}
.topbar li{color:#dfe3ea;font-size:8.4px;padding:0 15px;border-right:1px solid #3d4a60;line-height:10px}
.topbar li:first-child{padding-left:0}
.topbar li:last-child{border:none}
.quote-tab{left:569px;top:0;width:109px;height:30px;background:var(--red);color:#fff;font-size:8.4px;font-weight:700;display:flex;align-items:center;justify-content:center;clip-path:polygon(6px 0,100% 0,100% 100%,0 100%)}

/* header */
.logo-box{left:51px;top:30px;width:222px;height:56px;background:#f3f3f3;display:flex;align-items:center;padding-left:10px;gap:8px}
.logo-box .dot{width:26px;height:26px;border-radius:50%;background:var(--blue)}
.logo-box .name{font-weight:800;font-size:14px;color:var(--blue);letter-spacing:.3px}
.contact{top:50px;display:flex;gap:7px;align-items:center}
.contact .ico{width:20px;height:20px;background:#e3e3e3;display:flex;align-items:center;justify-content:center}
.contact small{display:block;font-size:7px;color:var(--muted)}
.contact b{display:block;font-size:8.4px;color:#333;font-weight:600}

/* hero */
.hero{left:0;top:88px;width:739px;height:290px;background:linear-gradient(90deg,#1f1f21 0%,#3a3a3c 40%,#4b4d52 65%,#2c2e33 100%)}
.hero-figure{left:440px;top:98px;width:270px;height:280px;background:radial-gradient(ellipse at 55% 55%,#b9a58a 0%,#8d9aae 45%,rgba(60,64,72,0) 75%)}
.hero-title{left:61px;top:176px;color:#fff;font-weight:700;font-stretch:75%;line-height:1;white-space:nowrap}
.hero-sub{font-size:27px;display:block}
.hero-main{font-size:38px;display:block;margin-top:6px}
.btn{position:absolute;display:flex;align-items:center;justify-content:center;font-size:8.4px;font-weight:600}
.btn.red{background:var(--red);color:#fff;clip-path:polygon(4px 0,100% 0,calc(100% - 4px) 100%,0 100%)}
.btn.white{background:#fff;color:var(--blue);clip-path:polygon(4px 0,100% 0,calc(100% - 4px) 100%,0 100%)}
.btn.blue{background:var(--blue);color:#fff;clip-path:polygon(3px 0,100% 0,calc(100% - 3px) 100%,0 100%)}
.rule{position:absolute;height:2px}

/* services */
.services{left:0;top:378px;width:739px;height:278px;background:var(--grey-band)}
.section-title{left:0;top:414px;width:739px;text-align:center;font-size:14px;color:var(--ink)}
.section-title span{color:var(--blue)}
.slashes{color:var(--red);font-size:8px;font-style:italic;letter-spacing:-1px}
.card{top:470px;width:295px;height:146px;background:#fff;box-shadow:0 2px 3px rgba(0,0,0,.08)}
.card.left{left:62px;border-radius:0 32px 0 32px}
.card.right{left:383px;border-radius:32px 0 32px 0}
.card .photo{position:absolute;left:10px;top:28px;width:138px;height:100px;border-radius:4px}
.card h3{position:absolute;left:153px;top:17px;font-size:15.5px;font-weight:600;color:var(--ink);width:126px;padding-bottom:5px;border-bottom:1px solid #ddd}
.card p{position:absolute;left:154px;top:48px;width:120px;font-size:7.6px;line-height:12px;color:#333}

/* about */
.eyebrow{font-size:10px;color:var(--ink)}
.big-title{font-size:14.5px;color:var(--blue);margin-top:2px;white-space:nowrap}
.about .big-title{font-size:13px;letter-spacing:-.3px}
.about{left:62px;top:692px;width:348px}
.about p{font-size:7.6px;line-height:14.3px;color:#333;margin-top:6px}
.about p+p{margin-top:9px}
.vline{left:434px;top:680px;width:1px;height:190px;background:linear-gradient(#fff,#ddd,#fff)}
.quote{left:463px;top:692px;width:215px}
.field{position:absolute;border:1px solid #cfcfcf;background:#fff;font-size:7.4px;color:#444;padding:6px 6px}
.divider-line{position:absolute;height:1px;background:#d6d6d6}

/* questions */
.band{left:0;top:928px;width:739px;height:85px;background:linear-gradient(90deg,#b9dbe8,#e6f2f6)}
.band-blue{left:0;top:928px;width:456px;height:85px;background:var(--blue);clip-path:polygon(0 0,100% 0,406px 100%,0 100%)}
.band-photo{left:580px;top:928px;width:159px;height:85px;background:linear-gradient(90deg,rgba(220,190,170,0),#d8b9a3 45%,#c9a58f)}
.band-title{left:61px;top:945px;font-size:19px;color:#fff;font-weight:400;white-space:nowrap}
.band-call{left:61px;top:972px;font-size:17px;color:#fff;white-space:nowrap}

/* footer */
.footer{left:0;top:1013px;width:739px;height:187px;background:var(--footer)}
.fcol{top:1037px}
.fcol h4{font-size:8.8px;font-weight:600;color:#fff;padding-bottom:7px;border-bottom:1px solid var(--footer-line)}
.fcol ul{list-style:none;margin-top:8px}
.fcol li{font-size:7.6px;color:#ddd;line-height:15.6px;padding-left:11px;position:relative}
.fcol li::before{content:"";position:absolute;left:1px;top:6px;width:3px;height:3px;border-radius:50%;background:#999}
.fsep{top:1037px;width:1px;height:100px;background:var(--footer-line)}
.fcol p{font-size:7.6px;color:#ddd;line-height:12px}
.nowrap{white-space:nowrap}
.social li{padding-left:0;display:flex;align-items:center;gap:8px;line-height:19px}
.social li::before{display:none}
.social .sq{width:12px;height:12px;background:#fff}
.copy-line{left:61px;top:1169px;width:617px;border-top:1px dotted #666}
.copy{left:0;top:1180px;width:739px;text-align:center;font-size:7.4px;color:#ddd}
</style>
</head>
<body>

<nav class="abs topbar">
  <ul><li>HOME</li><li>COURIER</li><li>FREIGHT</li><li>ABOUT US</li><li>CONTACT US</li><li>CUSTOMER LOGIN</li></ul>
</nav>
<div class="abs quote-tab">GET QUICK QUOTE</div>

<header>
  <div class="abs logo-box"><span class="dot"></span><span class="name">Bright Arrow Express</span></div>
  <div class="abs contact" style="left:387px">
    <div class="ico"><svg width="10" height="10" viewBox="0 0 24 24"><path fill="#0455a3" d="M6.6 10.8a15 15 0 0 0 6.6 6.6l2.2-2.2c.3-.3.7-.4 1-.2 1.1.4 2.3.6 3.6.6.6 0 1 .4 1 1V20c0 .6-.4 1-1 1A17 17 0 0 1 3 4c0-.6.4-1 1-1h3.5c.6 0 1 .4 1 1 0 1.3.2 2.5.6 3.6.1.3 0 .7-.2 1z"/></svg></div>
    <div><small>Respond in 24 hours</small><b>123 456 7890</b></div>
  </div>
  <div class="abs contact" style="left:509px">
    <div class="ico"><svg width="11" height="9" viewBox="0 0 22 16"><rect x="1" y="1" width="20" height="14" fill="none" stroke="#0455a3" stroke-width="2"/><path d="M1 1l10 8 10-8" fill="none" stroke="#0455a3" stroke-width="2"/></svg></div>
    <div><small>Email Us</small><b>info@brightarrowdelivery-sample.com</b></div>
  </div>
</header>

<section>
  <div class="abs hero" role="img" aria-label="Photo of a smiling courier in a cap carrying a cardboard box in front of a warehouse doorway"></div>
  <div class="abs hero-figure" role="img" aria-label="Courier holding a delivery box"></div>
  <h1 class="abs hero-title"><span class="hero-sub">We Go Where</span><span class="hero-main">The Freight Leads Us</span></h1>
  <div class="btn red" style="left:61px;top:268px;width:93px;height:24px">GET QUICK QUOTE</div>
  <div class="rule" style="left:52px;top:293px;width:100px;background:var(--red)"></div>
  <div class="btn white" style="left:154px;top:274px;width:94px;height:24px">Call Us Today</div>
  <div class="rule" style="left:156px;top:269px;width:100px;background:#fff"></div>
</section>

<section>
  <div class="abs services"></div>
  <h2 class="abs section-title wide">CHOOSE A <span>SERVICE DIVISION</span></h2>
  <div class="divider-line" style="left:300px;top:444px;width:139px"></div>
  <div class="abs slashes" style="left:364px;top:438px;background:var(--grey-band);padding:0 3px">///</div>

  <article class="abs card left">
    <div class="photo" role="img" aria-label="Courier with a hand truck of boxes beside a white delivery van" style="background:linear-gradient(90deg,#c9a47a 0%,#d9d9d9 40%,#f0f0f0 100%)"></div>
    <h3>Freight Picked</h3>
    <p>Lorem Ipsum is simply dummy text of the printing and typeset ting industry. Lorem Ipsum has been the industry's standard</p>
    <div class="btn blue" style="left:154px;top:98px;width:62px;height:20px">Read More</div>
    <div class="rule" style="left:154px;top:120px;width:68px;background:var(--blue)"></div>
  </article>

  <article class="abs card right">
    <div class="photo" role="img" aria-label="White box van with a cargo body" style="background:linear-gradient(180deg,#f4f4f4 0%,#e2e2e2 70%,#9a9a9a 100%)"></div>
    <h3>Transported</h3>
    <p>Lorem Ipsum is simply dummy text of the printing and typeset ting industry.</p>
    <div class="btn blue" style="left:154px;top:98px;width:62px;height:20px">Read More</div>
    <div class="rule" style="left:154px;top:120px;width:68px;background:var(--blue)"></div>
  </article>
</section>

<section>
  <div class="abs about">
    <div class="eyebrow wide">ABOUT</div>
    <div class="big-title wide">BRIGHT ARROW EXPRESS DELIVERY</div>
    <div style="position:relative;height:14px"><span class="slashes" style="position:absolute;left:0;top:1px">///</span><div class="divider-line" style="left:34px;top:7px;width:314px"></div></div>
    <p>Contrary to popular belief, Lorem Ipsum is not simply random text. It has roots in a piece of classical Latin literature from 45 BC, making it over 2000 years old. Daniel Hartwell, a Latin professor at Larchmont College in Virginia, looked up one of the more obscure Latin words, consectetur, from a Lorem Ipsum passage, and going through the cites of the word in classical literature, discovered the undoubtable source.</p>
    <p>Sardonic taped and underneath stung hawk yikes the where realistically this wow cut with jeez far treacherously far condescending invidiously menially and constitutionally ..</p>
  </div>
  <div class="btn red" style="left:62px;top:869px;width:62px;height:20px">Read More</div>
  <div class="rule" style="left:66px;top:890px;width:64px;background:var(--red)"></div>

  <div class="abs vline"></div>

  <div class="abs quote">
    <div class="eyebrow wide">GET</div>
    <div class="big-title wide">QUICK QUOTE</div>
    <div style="position:relative;height:14px"><span class="slashes" style="position:absolute;left:0;top:1px">///</span><div class="divider-line" style="left:34px;top:7px;width:181px"></div></div>
  </div>
  <div class="field" style="left:463px;top:753px;width:215px;height:22px">Name</div>
  <div class="field" style="left:463px;top:784px;width:105px;height:22px">Email Address</div>
  <div class="field" style="left:575px;top:784px;width:103px;height:22px">Phone</div>
  <div class="field" style="left:463px;top:814px;width:215px;height:39px">Message</div>
  <div class="btn red" style="left:465px;top:869px;width:62px;height:20px">Sumit</div>
  <div class="rule" style="left:469px;top:890px;width:64px;background:var(--red)"></div>
</section>

<section>
  <div class="abs band"></div>
  <div class="abs band-photo" role="img" aria-label="Smiling support agent wearing a headset"></div>
  <div class="abs band-blue"></div>
  <h2 class="abs band-title wide">QUESTIONS?</h2>
  <div class="abs band-call">Give us a call. 0-123-456-8180</div>
</section>

<footer>
  <div class="abs footer"></div>
  <div class="abs fcol" style="left:62px;width:84px">
    <h4>QUICK LINKS</h4>
    <ul><li>Home</li><li>Courier</li><li>Freight</li><li>About Us</li><li>Contact Us</li><li>Customer Login</li></ul>
  </div>
  <div class="abs fsep" style="left:165px"></div>
  <div class="abs fcol" style="left:188px;width:154px">
    <h4>SUBSCRIBE TO NEWSLETTER</h4>
    <p style="margin-top:8px">get latest updates by entering your email address</p>
    <div class="field" style="position:relative;margin-top:7px;height:21px;font-style:italic;border-color:#fff">Email Address</div>
    <div class="btn red" style="left:2px;top:93px;width:60px;height:18px">Subscribe</div>
    <div class="rule" style="left:6px;top:112px;width:62px;background:var(--red)"></div>
  </div>
  <div class="abs fsep" style="left:361px"></div>
  <div class="abs fcol" style="left:385px;width:149px">
    <h4>CONTACT INFORMATION</h4>
    <div style="position:relative;margin-top:10px;padding-left:15px">
      <svg style="position:absolute;left:0;top:1px" width="8" height="11" viewBox="0 0 16 22"><path fill="#fff" d="M8 0a8 8 0 0 0-8 8c0 6 8 14 8 14s8-8 8-14a8 8 0 0 0-8-8zm0 11a3 3 0 1 1 0-6 3 3 0 0 1 0 6z"/></svg>
      <p style="font-weight:600;color:#fff">bright arrow express delivery</p>
      <p>12, Sardonic taped and underneath stung hawk yikes the where</p>
    </div>
    <div style="position:relative;margin-top:11px;padding-left:15px">
      <svg style="position:absolute;left:0;top:1px" width="9" height="9" viewBox="0 0 24 24"><path fill="#fff" d="M6.6 10.8a15 15 0 0 0 6.6 6.6l2.2-2.2c.3-.3.7-.4 1-.2 1.1.4 2.3.6 3.6.6.6 0 1 .4 1 1V20c0 .6-.4 1-1 1A17 17 0 0 1 3 4c0-.6.4-1 1-1h3.5c.6 0 1 .4 1 1 0 1.3.2 2.5.6 3.6.1.3 0 .7-.2 1z"/></svg>
      <p style="font-weight:600;color:#fff">0-123-456-7890</p>
    </div>
    <div style="position:relative;margin-top:9px;padding-left:15px">
      <svg style="position:absolute;left:0;top:3px" width="9" height="7" viewBox="0 0 22 16"><rect x="1" y="1" width="20" height="14" fill="none" stroke="#fff" stroke-width="2"/><path d="M1 1l10 8 10-8" fill="none" stroke="#fff" stroke-width="2"/></svg>
      <p class="nowrap" style="font-size:7.2px">info@brightarrowdelivery-sample.com</p>
    </div>
  </div>
  <div class="abs fsep" style="left:557px"></div>
  <div class="abs fcol social" style="left:581px;width:96px">
    <h4>Follow Us</h4>
    <ul><li><span class="sq"></span>Friendbook</li><li><span class="sq"></span>Chirper</li><li><span class="sq"></span>Circles</li><li><span class="sq"></span>Worknet</li></ul>
  </div>
  <div class="abs copy-line"></div>
  <div class="abs copy">© 2016 Brightarrowdelivery-sample.com &nbsp;|&nbsp; All Rights Reserved</div>
</footer>

</body>
</html>
```